Radiant Harvest Gathering 2021

I am looking to create a flyer for a one day prayer retreat our church is organizing. This flyer will be posted on social media, websites, mobile apps, and will also be printed so it can be mailed to people.

I am looking for something professional, with good use of our logo and band colors (logo colors).

I am counting on the designer's skill, creativity, art and knowledge of media communication to produce a flyer that will effectively and quickly convey the message we are trying to spread.

CONTENT OF THE FLYER:
Event title: Radiant Harvest Gathering
Date: Tuesday July 2nd, 2021
Time: 11:00AM - 7:00PM
Bellmore Hotel, 4817 Wexley Avenue, Portland, Maine 04109 (Room: Tamarind)
Event Key words to highlight what the event is about: Prayer, Fasting, Worship, Prophecy, Revival.
Key phrases:
A one day prayer retreat.
Jesus Chris is Lord

Contact info:
www.quvello.org
Phone: 207 555 0148
Email: contact@brookmeadow.org

```html
<!DOCTYPE html>
<html lang="en">
<head>
<meta charset="utf-8">
<title>Radiant Harvest Gathering 2021</title>
<link rel="stylesheet" href="https://fonts.googleapis.com/css2?family=Almendra+Display&family=Almendra:wght@400;700&family=Cardo:wght@400;700&family=Arimo:wght@700&display=swap">
<style>
  :root {
    --ink-light: #fdf6ea;
    --ink-cream: #fbeed6;
    --sky-gold: #f0a530;
    --sky-amber: #c97a24;
    --sky-bronze: #8a4e1c;
    --earth-dark: #2a1508;
    --cross-grey: #e6e3df;
  }
  * { margin: 0; padding: 0; box-sizing: border-box; }
  html, body { width: 927px; height: 1200px; overflow: hidden; background: var(--earth-dark); }
  .flyer {
    position: relative;
    width: 927px;
    height: 1200px;
    overflow: hidden;
    color: var(--ink-light);
    font-family: "Cardo", serif;
  }
  .backdrop {
    position: absolute;
    inset: 0;
    background:
      radial-gradient(ellipse 260px 200px at 300px 470px, rgba(255,236,170,0.85), rgba(255,200,90,0) 70%),
      radial-gradient(ellipse 520px 380px at 480px 600px, rgba(245,175,60,0.55), rgba(245,175,60,0) 75%),
      linear-gradient(180deg, var(--sky-bronze) 0%, var(--sky-amber) 22%, var(--sky-gold) 45%, #e9a24a 62%, #c4823e 78%, #5a3214 92%, var(--earth-dark) 100%);
  }
  .title {
    position: absolute;
    top: 86px;
    left: 0;
    width: 100%;
    text-align: center;
    font-family: "Almendra Display", "Almendra", serif;
    font-size: 98px;
    line-height: 1;
    color: var(--ink-light);
  }
  .subtitle {
    position: absolute;
    top: 212px;
    left: 0;
    width: 100%;
    text-align: center;
    font-family: "Cardo", serif;
    font-weight: 700;
    font-size: 50px;
    letter-spacing: 1px;
    line-height: 1;
  }
  .tagline {
    position: absolute;
    top: 285px;
    left: 0;
    width: 100%;
    text-align: center;
    font-weight: 700;
    font-size: 21px;
    letter-spacing: 0.5px;
  }
  .keywords {
    position: absolute;
    top: 392px;
    left: 595px;
    list-style: none;
    font-family: "Almendra", serif;
    font-size: 29px;
    line-height: 43.5px;
  }
  .cross {
    position: absolute;
    top: 401px;
    left: 728px;
    width: 134px;
    height: 170px;
  }
  .when {
    position: absolute;
    top: 760px;
    left: 486px;
    font-weight: 700;
    font-size: 27px;
    line-height: 33px;
  }
  .venue {
    position: absolute;
    top: 852px;
    left: 486px;
    font-style: normal;
    font-weight: 700;
    font-size: 21.5px;
    line-height: 27.5px;
  }
  .confession {
    position: absolute;
    top: 1012px;
    left: 486px;
    font-family: "Almendra", serif;
    font-size: 36px;
    line-height: 1;
  }
  .org-name {
    position: absolute;
    top: 1036px;
    left: 68px;
    font-family: "Cardo", serif;
    font-weight: 400;
    font-size: 50px;
    letter-spacing: 1px;
    color: var(--ink-light);
    line-height: 1;
  }
  .contacts {
    position: absolute;
    top: 1105px;
    left: 352px;
    display: flex;
    gap: 20px;
    list-style: none;
    font-family: "Arimo", sans-serif;
    font-weight: 700;
    font-size: 12.5px;
    letter-spacing: 0.4px;
  }
  .contacts li { display: flex; align-items: center; gap: 5px; }
  .contacts svg { width: 11px; height: 11px; flex: none; }
  .contacts .icon { stroke: var(--sky-gold); fill: none; stroke-width: 1.6; }
</style>
</head>
<body>
<main class="flyer">
  <div class="backdrop" role="img" aria-label="Silhouette of an open hand reaching toward a glowing golden sunset sky above dark grass"></div>

  <h1 class="title">Radiant Harvest</h1>
  <p class="subtitle">GATHERING</p>
  <p class="tagline">A ONE DAY PRAYER RETREAT</p>

  <ul class="keywords">
    <li>Prayer</li>
    <li>Fasting</li>
    <li>Worship</li>
    <li>Prophecy</li>
    <li>Revival</li>
  </ul>

  <svg class="cross" viewBox="0 0 134 170" aria-hidden="true">
    <rect x="57" y="0" width="22" height="170" fill="var(--cross-grey)"/>
    <rect x="0" y="42" width="134" height="24" fill="var(--cross-grey)"/>
  </svg>

  <p class="when">Tuesday, July 2nd, 2021<br>11:00AM - 7:00PM</p>

  <address class="venue">
    Bellmore Hotel<br>
    Tamarind Room<br>
    4817 Wexley Avenue<br>
    Portland, Maine 04109
  </address>

  <p class="confession">Jesus Christ is Lord</p>

  <p class="org-name">QUVELLO</p>

  <ul class="contacts">
    <li>
      <svg viewBox="0 0 12 12" aria-hidden="true"><circle class="icon" cx="6" cy="6" r="5"/><path class="icon" d="M1 6h10M6 1c2 2 2 8 0 10M6 1c-2 2-2 8 0 10"/></svg>
      WWW.QUVELLO.ORG
    </li>
    <li>
      <svg viewBox="0 0 12 12" aria-hidden="true"><path class="icon" d="M3 1l2 2.5-1.2 1.5c.8 1.5 1.7 2.4 3.2 3.2L8.5 7 11 9l-1.5 2C5 10.5 1.5 7 1 2.5z"/></svg>
      207 555 0148
    </li>
    <li>
      <svg viewBox="0 0 12 12" aria-hidden="true"><rect class="icon" x="1" y="2.5" width="10" height="7"/><path class="icon" d="M1 2.5l5 4 5-4"/></svg>
      CONTACT@BROOKMEADOW.ORG
    </li>
  </ul>
</main>
</body>
</html>
```